Business card for Kestrel Bathrooms

Please design a business card for our bathroom renovation business. You can use my existing logo, but if you have an idea to modernize it, I would like to see it. Please see attached files first. I would like to use the blue and the orange theme. I like the concept of using the shower head in the logo. Please find following a design (or two) that I have been trying to create with my limited resources. That design was for a sign, but I was going to adopt it and use it as a business card as well. I like the concept of the water splash but I don’t think it “flows” nicely together with the logo. Another thought is that maybe creating the logo out of water splash could work and have a dramatic effect (like the water text and the butterfly picture attached with similar background instead of white). If the above doesn’t work I would like to see a modern simplified design. One of the attached files named as the unwanted business card has all the details that I want included in the business card. Please note that it is two sided.
Updates

I am very thankful for the designs that I have received, but they are very similar and only a couple of attempts to do something with the water splash as per my original brief. Modernizing the logo and having it made out of out of water splash with the orange as color accent could work and have a dramatic effect (like the water text and the butterfly picture attached with similar background instead of white). Please do not use the butterfly itself! This is just an example that images can be created out of water splash.

Contact Information for Business Card

all the details are on the unwonted business card file included

Colors
3176b5

Requirements
Nice to have
• Copied from the brief:
• ... maybe creating the logo out of water splash could work and have a dramatic effect (like the water text and the butterfly picture attached with similar background instead of white). Please do not use the butterfly itself!
Should not have
• I am getting designs with a butterfly. The butterfly picture was an example of creating something from a water splash. The butterfly itself has no association with anything other than the concept of creating a logo out of water splash. Sorry, I thought I was clear in the brief.

```html
<!DOCTYPE html>
<html lang="en">
<head>
<meta charset="utf-8">
<title>Kestrel Bathrooms – Business Card</title>
<link href="https://fonts.googleapis.com/css2?family=Lato:wght@400;700&display=swap" rel="stylesheet">
<style>
  :root{
    --navy:#1f3f6e;
    --coral:#e8735f;
    --ink:#22385b;
    --paper:#ffffff;
    --backdrop:#e9ebef;
    --splash-light:#eaf3f9;
    --splash-mid:#9cc4de;
    --wing:#8fa3bd;
  }
  *{margin:0;padding:0;box-sizing:border-box}
  html,body{width:1200px;height:800px;overflow:hidden}
  body{background:var(--backdrop);font-family:"Lato",Arial,sans-serif;color:var(--ink);position:relative}

  .card{position:absolute;width:560px;height:320px;background:var(--paper);
    box-shadow:0 10px 30px rgba(20,30,50,.18);overflow:hidden}
  .card--front{left:60px;top:50px}
  .card--back{left:580px;top:430px}

  .edge-band{position:absolute;left:0;right:0;bottom:0;height:9px;display:flex}
  .edge-band__navy{flex:0 0 62%;background:var(--navy)}
  .edge-band__coral{flex:1;background:var(--coral)}

  .brand{position:absolute;display:flex;align-items:center;gap:12px}
  .brand__dot{width:22px;height:22px;border-radius:50%;background:var(--coral);flex:none}
  .brand__name{font-weight:700;font-size:30px;line-height:1.05;color:var(--navy);letter-spacing:.5px}

  /* front */
  .card--front .brand{left:44px;top:120px}
  .splash{position:absolute;right:0;bottom:9px;width:330px;height:190px;
    background:radial-gradient(ellipse at 70% 80%,var(--splash-mid) 0%,var(--splash-light) 55%,rgba(255,255,255,0) 80%)}
  .divider{position:absolute;left:300px;top:70px;width:1px;height:150px;background:var(--coral)}
  .contact{position:absolute;left:322px;top:58px;font-size:13px;line-height:1.5}
  .contact__name{color:var(--coral);font-weight:700;text-transform:uppercase;font-size:14px;margin-bottom:10px;letter-spacing:.3px}
  .contact__accent{color:var(--coral)}
  .contact__web{color:var(--coral);margin-top:2px}

  /* back */
  .card--back .brand{left:40px;top:40px}
  .wing-art{position:absolute;right:34px;top:26px;width:200px;height:120px;border-radius:50% 50% 40% 40%;
    background:radial-gradient(ellipse at center,var(--wing) 0%,#d5dde8 60%,rgba(255,255,255,0) 75%)}
  .services{position:absolute;left:40px;top:170px}
  .services__title{color:var(--coral);font-size:15px;font-weight:700;text-transform:uppercase;margin-bottom:8px;letter-spacing:.3px}
  .services__list{list-style:none;font-size:12.5px;line-height:1.6;text-transform:uppercase;color:var(--ink)}
  .services__list li{display:flex;align-items:center;gap:10px}
  .services__list li::before{content:"";width:8px;height:8px;border-radius:50%;background:var(--coral);flex:none}
</style>
</head>
<body>

<section class="card card--front" aria-label="Business card front">
  <div class="brand">
    <span class="brand__dot"></span>
    <span class="brand__name">Kestrel<br>Bathrooms</span>
  </div>
  <div class="splash" role="img" aria-label="Blue water splash rising from the lower edge"></div>
  <div class="divider"></div>
  <address class="contact" style="font-style:normal">
    <div class="contact__name">Daniel Mercer</div>
    <div>PO Box 41</div>
    <div>Tallowood 2620</div>
    <div>0400 555 218 | 6200 4417</div>
    <div><span class="contact__accent">E:</span> daniel@kestrelbathrooms.com.au</div>
    <div class="contact__web">kestrelbathrooms.com.au</div>
  </address>
  <div class="edge-band"><span class="edge-band__navy"></span><span class="edge-band__coral"></span></div>
</section>

<section class="card card--back" aria-label="Business card back">
  <div class="brand">
    <span class="brand__dot"></span>
    <span class="brand__name">Kestrel<br>Bathrooms</span>
  </div>
  <div class="wing-art" role="img" aria-label="Winged shape formed from splashing water"></div>
  <div class="services">
    <h2 class="services__title">Our Services</h2>
    <ul class="services__list">
      <li>Complete bathroom renovations &amp; remodelling</li>
      <li>Highly skilled &amp; qualified tradespeople</li>
      <li>Professional service from concept to completion</li>
      <li>All work guaranteed</li>
    </ul>
  </div>
  <div class="edge-band"><span class="edge-band__navy"></span><span class="edge-band__coral"></span></div>
</section>

</body>
</html>
```